Design a Website Mockup for our new product design website

We are looking to create a homepage mockup for http://www.TarnwickDesign.com to give the site an updated look.
We want also to include on the main page "Featured Product Design" where we show 10 products and a Video box to show our new youtube video.
http://www.vidplexo.com/watch?v=KQT8ZNAHXwd

We need all the info that is currently listed on the site to still be visible however the layout and design can completely change. Please make sure that it still coordinates with the sites logo and captures what our company does - design new products and bring it to market.
If you have any questions please feel free to ask!!!

Winner, will not only win this site new design, but will also win the opportunity to do web design for our clients!

```html
<!DOCTYPE html>
<html lang="en">
<head>
<meta charset="utf-8">
<title>TarnwickDesign – Product Design &amp; Development</title>
<link href="https://fonts.googleapis.com/css2?family=Raleway:wght@300;400;600;700;800&family=Comfortaa:wght@400;700&family=Roboto+Condensed:wght@400&family=Open+Sans:wght@400;600;700&display=swap" rel="stylesheet">
<style>
:root{
  --green:#7aa34a;
  --green-dark:#5f8a35;
  --charcoal:#3c3c3c;
  --footer:#262626;
  --orange:#f39a1e;
  --ink:#222;
  --muted:#666;
  --quote:#bdbdbd;
}
*{box-sizing:border-box;margin:0;padding:0}
html,body{width:1200px;height:2285px;overflow:hidden;background:#fff}
body{position:relative;font-family:"Open Sans",sans-serif;color:var(--ink)}
.abs{position:absolute}
svg{display:block}

.topbar{left:0;top:0;width:1200px;height:27px;background:var(--green);color:#eef5e4;font-size:11px}
.topbar .contact{left:120px;top:6px;display:flex;gap:8px;align-items:center}
.topbar .follow{right:120px;top:5px;display:flex;gap:14px;align-items:center;font-size:9px}
.topbar .follow i{display:block;width:10px;height:10px;border-radius:50%;background:#eef5e4;opacity:.85}

.header{left:0;top:27px;width:1200px;height:66px;background:var(--charcoal)}
.brand{display:flex;align-items:center;gap:6px;color:#fff;font-family:"Raleway",sans-serif;font-size:14px;font-weight:600}
.brand .dot{width:40px;height:40px;border-radius:50%;background:var(--green)}

.slider{left:0;top:93px;width:1200px;height:440px;background:linear-gradient(#d4d4d4,#f2f2f2 60%,#fff)}
.nav{left:242px;top:101px;display:flex;gap:24px;font-size:16px;font-weight:600;color:#222}
.nav .active{color:#fff}
.dropdown{left:232px;top:123px;width:143px;background:rgba(70,70,70,.85)}
.dropdown li{list-style:none;color:#fff;font-size:10.5px;padding:5px 10px;border-bottom:1px solid rgba(255,255,255,.18);white-space:nowrap}
.slide{width:180px;height:248px;top:162px}
.caption{font-family:"Roboto Condensed",sans-serif;font-size:17px;color:#333;top:434px;width:240px;text-align:center}
.arrow{top:270px}
.dots{left:556px;top:498px;display:flex;gap:7px}
.dots i{width:9px;height:9px;border-radius:50%;background:var(--green)}
.dots i.on{background:#333}

.welcome-title{left:0;top:566px;width:1200px;text-align:center;font-family:"Comfortaa",sans-serif;font-size:32px;font-weight:700;color:#111}
.intro{left:152px;top:645px;width:366px;font-size:13px;line-height:19.8px;text-align:justify;color:#333}
.intro p{text-indent:40px}
.intro .more{display:block;margin-top:2px;font-style:italic;font-weight:700;color:#111}
.video{left:626px;top:628px;width:450px;height:284px;border:3px solid #ccc;background:#222}
.video .title{left:8px;top:4px;color:#fff;font-size:12px}
.video .screen{left:0;top:22px;width:444px;height:222px;background:linear-gradient(160deg,#5a5a5a,#2a2a2a 55%,#3c4a8a)}
.video .controls{left:0;bottom:0;width:444px;height:40px;background:#1a1a1a}

.band{left:0;top:1000px;width:1200px;height:49px;background:var(--green)}
.band h2{position:absolute;left:120px;top:6px;font-family:"Raleway",sans-serif;font-weight:300;font-size:32px;color:#fff}
.band h2 b{font-weight:700}
.search{right:130px;top:13px;width:200px;height:24px;border:1px solid #a7c77f;border-radius:12px;font-size:11px;color:#b9d59a;font-style:italic;padding:4px 12px}
.card{width:194px;height:192px}
.card.sel{background:var(--green)}
.card .img{left:3px;top:3px;width:188px;height:131px}
.card h4{position:absolute;left:5px;top:135px;font-size:12px;font-weight:700}
.card p{position:absolute;left:5px;top:151px;width:180px;font-size:10px;line-height:12px;color:#555}
.card.sel h4,.card.sel p{color:#fff}
.card .btn{position:absolute;right:3px;top:167px;width:76px;height:17px;background:var(--orange);color:#fff;font-size:10px;text-align:center;line-height:17px}
.more-link{left:372px;top:1555px;font-family:"Raleway",sans-serif;font-size:22px;font-weight:800;display:flex;align-items:center;gap:5px}

.latest-title{left:803px;top:1067px;width:273px;text-align:center;font-family:"Raleway",sans-serif;font-size:23px;line-height:26px;font-weight:400;color:#111}
.latest-title b{font-weight:700}
.latest{left:803px;top:1095px;width:273px;height:520px;background:var(--green-dark);border:3px solid #8fb562}
.latest .item{position:absolute;left:3px;width:255px;height:80px;border-bottom:1px dashed #a9c98a}
.latest .thumb{position:absolute;left:3px;top:5px;width:71px;height:72px;background:linear-gradient(90deg,#e8e8e8,#2b2b2b 45%,#e8e8e8)}
.latest h5{position:absolute;left:84px;top:8px;color:#fff;font-size:10px;font-weight:700}
.latest p{position:absolute;left:84px;top:22px;width:165px;color:#eaf2df;font-size:8px;line-height:9.5px}
.latest .scroll{position:absolute;right:0;top:0;width:6px;height:96px;background:var(--orange)}

.clients-title{left:0;top:1680px;width:1200px;text-align:center;font-family:"Raleway",sans-serif;font-size:32px;font-weight:300}
.clients-title b{font-weight:700}
.clients{left:0;top:1776px;width:1200px;height:168px;border-top:3px solid var(--orange);border-bottom:3px solid var(--orange)}
.client{top:84px;display:flex;align-items:center;gap:8px;font-family:"Raleway",sans-serif;font-weight:700;font-size:28px;line-height:30px}
.client i{display:block;width:26px;height:26px;border-radius:50%}

.social-btn{top:1971px;height:30px;color:#fff;font-size:10px;display:flex;align-items:center;padding-left:10px}

.footer{left:0;top:2000px;width:1200px;height:247px;background:var(--footer);color:#bbb}
.footer h6{position:absolute;font-size:11px;letter-spacing:.5px;color:#fff;font-weight:600}
.footer ul{position:absolute;list-style:none;font-size:11.5px;line-height:20px}
.footer .info{position:absolute;left:135px;top:139px;font-size:10.5px;line-height:16px;color:#ddd}
.footer .circ{position:absolute;width:18px;height:18px;border-radius:50%}
.email-field{left:892px;top:2062px;width:186px;height:20px;background:#fff;font-size:10px;color:#aaa;padding:3px 12px}
.send{left:1012px;top:2094px;width:64px;height:20px;background:var(--orange);color:#fff;font-size:11px;font-weight:700;text-align:center;line-height:20px}
.to-top{left:1031px;top:2150px;width:44px;height:44px;background:var(--green)}
.bottombar{left:0;top:2247px;width:1200px;height:38px;background:var(--green);color:#fff;font-size:9px;line-height:11px;text-align:center;padding-top:3px}
</style>
</head>
<body>

<div class="abs topbar">
  <div class="abs contact">
    <svg width="10" height="14" viewBox="0 0 10 14"><rect x="1" y="1" width="8" height="12" rx="1.5" fill="none" stroke="#eef5e4"/></svg>
    <span>(800) 555-0187</span><span>|</span>
    <svg width="18" height="12" viewBox="0 0 18 12"><rect x="1" y="1" width="16" height="10" fill="none" stroke="#eef5e4"/><path d="M1 1l8 6 8-6" fill="none" stroke="#eef5e4"/></svg>
    <span>invent@tarnwickdesign.com</span>
  </div>
  <div class="abs follow"><span>Follow us on</span><i></i><i></i><i></i><i></i><i></i><i></i><i></i><i></i><i></i><i></i></div>
</div>

<div class="abs header">
  <div class="abs brand" style="left:120px;top:13px"><span class="dot"></span>TarnwickDesign</div>
</div>

<div class="abs slider"></div>
<nav class="abs nav">
  <span class="active">Product Design</span><span>Prototyping</span><span>Manufacturing</span><span>Patents</span><span>Web Design</span><span>Marketing</span><span>Blog</span><span>Contact</span>
</nav>

<div class="abs slide" style="left:180px;width:150px;background:linear-gradient(#eaeaea,#d9d9d9)" role="img" aria-label="Pencil concept sketch of an electric shaver"></div>
<div class="abs slide" style="left:420px;width:160px;background:linear-gradient(90deg,#d8dce8,#2f4fa0 55%,#1e2a55)" role="img" aria-label="Rendered blue and silver electric shaver"></div>
<div class="abs slide" style="left:675px;width:180px;background:linear-gradient(90deg,#2a3570,#b7b9c3 50%,#2a3570)" role="img" aria-label="Exploded mechanical view of the shaver internals"></div>
<div class="abs slide" style="left:925px;width:110px;background:linear-gradient(90deg,#1a1a1a,#555 50%,#1a1a1a)" role="img" aria-label="Final black shaver design"></div>

<ul class="abs dropdown">
  <li>• Concept Sketches</li><li>• 3D modelling</li><li>• Mechanical Engineering</li><li>• CAD Design</li><li>• Product Packaging</li><li>• POP Display</li>
</ul>

<div class="abs caption" style="left:131px">CONCEPT SKETCH</div>
<div class="abs caption" style="left:382px">ADVANCED SKETCH</div>
<div class="abs caption" style="left:648px">MECHANICAL ENGENEERING</div>
<div class="abs caption" style="left:856px">FINAL DESIGN</div>

<svg class="abs arrow" style="left:118px" width="22" height="40" viewBox="0 0 22 40"><path d="M18 4L4 20l14 16" fill="none" stroke="#aaa" stroke-width="3"/></svg>
<svg class="abs arrow" style="left:1052px" width="22" height="40" viewBox="0 0 22 40"><path d="M4 4l14 16L4 36" fill="none" stroke="#aaa" stroke-width="3"/></svg>
<div class="abs dots"><i></i><i class="on"></i><i></i><i></i><i></i></div>

<h1 class="abs welcome-title">Welcome to our Site</h1>
<svg class="abs" style="left:119px;top:627px" width="40" height="30" viewBox="0 0 40 30">
  <path d="M2 30V16C2 7 7 2 16 1v6c-4 1-6 4-6 8h6v15zM24 30V16c0-9 5-14 14-15v6c-4 1-6 4-6 8h6v15z" fill="var(--quote)"/>
</svg>
<svg class="abs" style="left:517px;top:800px" width="40" height="30" viewBox="0 0 40 30">
  <path d="M16 0v14c0 9-5 14-14 15v-6c4-1 6-4 6-8H2V0zM38 0v14c0 9-5 14-14 15v-6c4-1 6-4 6-8h-6V0z" fill="var(--quote)"/>
</svg>
<div class="abs intro">
  <p>TarnwickDesign is a complete service Product Design &amp; Development Company, located at Coral Point, Florida. TarnwickDesign can make your idea into a real product. We are a one stop shop for product development, taking you through our design and manufacturing methodology, which includes concept sketching, computer illustrations, engineering, 3D CAD, prototyping, patenting, manufacturing, packaging, logistics, and marketing.</p>
  <span class="more">Read more...</span>
</div>

<div class="abs video">
  <div class="abs title">Tarnwick Design: 3D modelling(from concept to final)</div>
  <div class="abs screen" role="img" aria-label="Video still of a blue concept race car with technical blueprints"></div>
  <div class="abs controls">
    <div class="abs" style="left:24px;top:2px;width:90px;height:3px;background:var(--orange)"></div>
    <svg class="abs" style="left:130px;top:8px" width="130" height="28" viewBox="0 0 130 28">
      <circle cx="14" cy="14" r="10" fill="none" stroke="#bbb" stroke-width="1.5"/><path d="M17 9l-5 5 5 5M12 9l-5 5 5 5" fill="none" stroke="#bbb"/>
      <circle cx="64" cy="14" r="12" fill="none" stroke="#fff" stroke-width="1.5"/><path d="M60 8l10 6-10 6z" fill="#fff"/>
      <circle cx="114" cy="14" r="10" fill="none" stroke="#bbb" stroke-width="1.5"/><path d="M111 9l5 5-5 5M116 9l5 5-5 5" fill="none" stroke="#bbb"/>
    </svg>
  </div>
</div>

<div class="abs band">
  <h2>Featured <b>Product Design</b></h2>
  <div class="abs search">search...</div>
</div>

<div class="abs card sel" style="left:117px;top:1093px">
  <div class="abs img" style="background:linear-gradient(#eef0f3,#9fb7d2 70%,#cfd5dd)" role="img" aria-label="Blue personal helicopter concept"></div>
  <h4>lorem ipsum</h4><p>It is a placeholder text commonly used to...</p><span class="btn">Details</span>
</div>
<div class="abs card" style="left:339px;top:1093px">
  <div class="abs img" style="background:radial-gradient(#2f4a3e,#9fb8b0)" role="img" aria-label="Quadcopter drone concept"></div>
  <h4>lorem ipsum</h4><p>It is a placeholder text commonly used to...</p><span class="btn">Details</span>
</div>
<div class="abs card" style="left:565px;top:1093px">
  <div class="abs img" style="background:linear-gradient(#6a3a20,#c07a45)" role="img" aria-label="White compact device on a wooden table"></div>
  <h4>lorem ipsum</h4><p>It is a placeholder text commonly used to...</p><span class="btn">Details</span>
</div>
<div class="abs card" style="left:117px;top:1317px">
  <div class="abs img" style="background:linear-gradient(#f4f4f4,#dcdcdc)" role="img" aria-label="Electric bicycle concept"></div>
  <h4>lorem ipsum</h4><p>It is a placeholder text commonly used to...</p><span class="btn">Details</span>
</div>
<div class="abs card" style="left:342px;top:1317px">
  <div class="abs img" style="background:linear-gradient(#f1f1f4,#9aa5d6)" role="img" aria-label="Curved lounge chair concept"></div>
  <h4>lorem ipsum</h4><p>It is a placeholder text commonly used to...</p><span class="btn">Details</span>
</div>
<div class="abs card" style="left:563px;top:1317px">
  <div class="abs img" style="background:linear-gradient(#2a2a2a,#7a7a7a)" role="img" aria-label="Small pod vehicle concept"></div>
  <h4>lorem ipsum</h4><p>It is a placeholder text commonly used to...</p><span class="btn">Details</span>
</div>

<div class="abs more-link">
  <svg width="18" height="18" viewBox="0 0 18 18"><circle cx="9" cy="9" r="7.5" fill="none" stroke="#111" stroke-width="1.8"/><path d="M5.5 7.5L9 11l3.5-3.5" fill="none" stroke="#111" stroke-width="1.8"/></svg>MORE...
</div>

<div class="abs latest-title">Latest <b>Designs</b></div>
<div class="abs latest">
  <span class="scroll"></span>
  <div class="item" style="top:0"><div class="thumb" role="img" aria-label="Wristband device"></div><h5>Lorem ipsum</h5><p>is a placeholder text commonly used to demonstrate the graphic elements of a document or visual presentation, such as font.</p></div>
  <div class="item" style="top:85px"><div class="thumb" role="img" aria-label="Wristband device"></div><h5>Lorem ipsum</h5><p>is a placeholder text commonly used to demonstrate the graphic elements of a document or visual presentation, such as font.</p></div>
  <div class="item" style="top:170px"><div class="thumb" role="img" aria-label="Wristband device"></div><h5>Lorem ipsum</h5><p>is a placeholder text commonly used to demonstrate the graphic elements of a document or visual presentation, such as font.</p></div>
  <div class="item" style="top:255px"><div class="thumb" role="img" aria-label="Wristband device"></div><h5>Lorem ipsum</h5><p>is a placeholder text commonly used to demonstrate the graphic elements of a document or visual presentation, such as font.</p></div>
  <div class="item" style="top:340px"><div class="thumb" role="img" aria-label="Wristband device"></div><h5>Lorem ipsum</h5><p>is a placeholder text commonly used to demonstrate the graphic elements of a document or visual presentation, such as font.</p></div>
  <div class="item" style="top:425px"><div class="thumb" role="img" aria-label="Wristband device"></div><h5>Lorem ipsum</h5><p>is a placeholder text commonly used to demonstrate the graphic elements of a document or visual presentation, such as font.</p></div>
</div>

<div class="abs clients-title">Our <b>Clients</b></div>
<svg class="abs" style="left:582px;top:1735px" width="52" height="22" viewBox="0 0 52 22">
  <circle cx="11" cy="11" r="10" fill="#222"/><path d="M13 6l-5 5 5 5" fill="none" stroke="#fff" stroke-width="2"/>
  <circle cx="37" cy="11" r="10" fill="var(--green)"/><path d="M35 6l5 5-5 5" fill="none" stroke="#fff" stroke-width="2"/>
</svg>

<div class="abs clients">
  <div class="abs client" style="left:70px;color:#1d4e8f">Ventora</div>
  <div class="abs client" style="left:290px;color:#555"><i style="border:3px solid #e0423a"></i>noddle</div>
  <div class="abs client" style="left:520px;color:#b07a10">Oakhollow</div>
  <div class="abs client" style="left:735px;color:#8cc13f">stedima</div>
  <div class="abs client" style="left:960px;color:#f08a1c"><i style="background:#f08a1c;border-radius:0"></i>Pulsewell</div>
</div>

<div class="abs social-btn" style="left:731px;width:164px;background:#3aa3df">Follow us on Chirply</div>
<div class="abs social-btn" style="left:916px;width:161px;background:#3b5998">Like us on Friendnest</div>

<footer class="abs footer">
  <div class="abs brand" style="left:132px;top:14px;font-size:19px"><span class="dot" style="width:68px;height:68px"></span>TarnwickDesign</div>
  <h6 style="left:135px;top:110px">CONTACT INFO</h6>
  <div class="info">4820 Larkspur Avenue Suite #210,<br>Coral Point, Florida,<br>33999<br>USA<br>Tel: (800) 555-0187<br>E-mail: invent@TarnwickDesign.com</div>

  <h6 style="left:475px;top:38px">NAVIGATION</h6>
  <ul style="left:475px;top:60px"><li>Home</li><li>Product Design</li><li>Prototyping</li><li>Manufacturing</li><li>Patents</li><li>Web Design</li><li>Marketing</li><li>Blog</li></ul>
  <h6 style="left:618px;top:38px">LINKS</h6>
  <ul style="left:618px;top:59px"><li>About Us</li><li>News</li><li>Our Clients</li><li>Contact Us</li><li>GET A QUOTE</li></ul>

  <h6 style="left:775px;top:39px">GET IN TOUCH</h6>
  <span class="circ" style="left:776px;top:62px;background:#3b5998"></span>
  <span class="circ" style="left:811px;top:62px;background:#3aa3df"></span>
  <span class="circ" style="left:846px;top:62px;background:#d9453a"></span>
  <span class="circ" style="left:776px;top:92px;background:#c8342a"></span>
  <span class="circ" style="left:811px;top:92px;background:#666"></span>
  <span class="circ" style="left:776px;top:122px;background:var(--orange)"></span>

  <h6 style="left:897px;top:38px">SUBSCRIPTION</h6>
  <div class="abs" style="left:1030px;top:196px;font-size:8px;color:#bbb">Back to Top</div>
</footer>
<div class="abs email-field">your.address@email.com</div>
<div class="abs send">SEND</div>
<svg class="abs to-top" width="44" height="44" viewBox="0 0 44 44"><path d="M22 34V11M12 21l10-10 10 10" fill="none" stroke="#fff" stroke-width="2.5"/></svg>

<div class="abs bottombar">All rights reserved TarnwickDesign © 2011.<br>TarnwickDesign 4820 Larkspur Avenue Suite #210, Coral Point, Florida, 33999, USA.<br>Tel: (800) 555-0187 E-mail: invent@TarnwickDesign.com</div>

</body>
</html>
```